Software engineering company needs business card

I need a cool business card. Company: Byte Merano Larchwood Ave 41 58213 Dunmere Name: Gerald Hofmann CEO / Managing Director & Owner

Industry/Entity Type

Business

```html
<!DOCTYPE html>
<html lang="en">
<head>
<meta charset="utf-8">
<title>Byte Merano – Business Card</title>
<link rel="stylesheet" href="https://fonts.googleapis.com/css2?family=Oswald:wght@500&family=Roboto:wght@400&display=swap">
<style>
  :root {
    --stage: #3a3a3a;
    --card-dark: #000000;
    --card-light: #ffffff;
    --accent: #7dc02f;
    --ink: #3d3d3d;
    --ink-soft: #555555;
  }
  * { margin: 0; padding: 0; box-sizing: border-box; }
  html, body { width: 1200px; height: 900px; overflow: hidden; }
  body {
    background: var(--stage);
    position: relative;
    font-family: "Roboto", Arial, sans-serif;
  }
  .card {
    position: absolute;
    left: 250px;
    width: 700px;
    height: 400px;
    box-shadow: 0 10px 30px rgba(0,0,0,0.45);
  }
  .card--back { top: 30px; background: var(--card-dark); }
  .card--front { top: 470px; background: var(--card-light); }

  .corner-mark {
    position: absolute;
    width: 34px;
    height: 24px;
    background: var(--accent);
    bottom: 24px;
  }
  .corner-mark--left { left: 22px; }
  .corner-mark--right { right: 22px; }

  .brand {
    position: absolute;
    display: flex;
    align-items: center;
    gap: 12px;
    font-family: "Oswald", Arial, sans-serif;
    font-weight: 500;
    color: var(--accent);
    letter-spacing: 4px;
    text-transform: uppercase;
    white-space: nowrap;
  }
  .brand__square { width: 18px; height: 18px; background: var(--accent); }
  .card--back .brand { left: 300px; top: 235px; font-size: 44px; }
  .card--front .brand { right: 40px; top: 60px; font-size: 34px; }

  .person { position: absolute; left: 40px; top: 170px; }
  .person__name {
    font-family: "Oswald", Arial, sans-serif;
    font-weight: 500;
    font-size: 30px;
    letter-spacing: 2px;
    text-transform: uppercase;
    line-height: 1;
  }
  .person__first { color: var(--accent); }
  .person__last { color: var(--ink); }
  .person__role { margin-top: 6px; font-size: 17px; color: var(--ink-soft); }

  .contact { position: absolute; left: 40px; top: 252px; list-style: none; }
  .contact__item {
    display: flex; align-items: center; gap: 12px;
    font-size: 17px; color: var(--ink-soft); line-height: 27px;
  }
  .contact__icon { width: 14px; height: 14px; flex: none; }

  .address {
    position: absolute; left: 40px; bottom: 30px;
    font-size: 17px; color: var(--ink-soft);
  }
</style>
</head>
<body>
  <section class="card card--back" aria-label="Card back">
    <div class="brand"><span class="brand__square"></span>Byte Merano</div>
    <span class="corner-mark corner-mark--left"></span>
    <span class="corner-mark corner-mark--right"></span>
  </section>

  <section class="card card--front" aria-label="Card front">
    <div class="brand"><span class="brand__square"></span>Byte Merano</div>

    <div class="person">
      <p class="person__name"><span class="person__first">Gerald</span> <span class="person__last">Hofmann</span></p>
      <p class="person__role">CEO / Managing Director &amp; Owner</p>
    </div>

    <ul class="contact">
      <li class="contact__item">
        <svg class="contact__icon" viewBox="0 0 14 14" aria-hidden="true"><path d="M3 1 L5 4 L4 5.5 Q5.5 8.5 8.5 10 L10 9 L13 11 L11.5 13 Q6 12.5 1 3 Z" fill="var(--accent)"/></svg>
        +1 555-204-7318
      </li>
      <li class="contact__item">
        <svg class="contact__icon" viewBox="0 0 14 14" aria-hidden="true"><rect x="1" y="3" width="12" height="8.5" fill="none" stroke="var(--accent)" stroke-width="1.4"/><path d="M1 3 L7 8 L13 3" fill="none" stroke="var(--accent)" stroke-width="1.4"/></svg>
        info@bytemerano.com
      </li>
      <li class="contact__item">
        <svg class="contact__icon" viewBox="0 0 14 14" aria-hidden="true"><circle cx="7" cy="7" r="6" fill="none" stroke="var(--accent)" stroke-width="1.3"/><ellipse cx="7" cy="7" rx="2.6" ry="6" fill="none" stroke="var(--accent)" stroke-width="1.1"/><path d="M1 7 H13" stroke="var(--accent)" stroke-width="1.1"/></svg>
        www.bytemerano.com
      </li>
    </ul>

    <p class="address">Larchwood Ave 41 58213 Dunmere</p>
  </section>
</body>
</html>
```